Public Speaking Book for aspiring, ambitious speakers

I'm looking for a 6x9 book cover (Parcelo standard) as well as ebook and audiobook formats.

I'm looking for orange font on a white background as these are my brand colours.

Feel free to use some yellow and gold too if you deem it appropriate.

Title: Climb and Glow
Subtitle: Find Your Voice. Tell Your Story. Share your Message.
Author: Lionel Barstow

I would like to have a picture of a female speaker on the front cover.

Alternatively, some kind of image that symbolises public speaking like a microphone, podium etc

Target Market(s)

Aspiring professional speakers

Colors
f78f20

Requirements
Must have
• Correct spelling!
Nice to have
• A logo or picture that fits the theme, but no pressure if you can't think of anything
Should not have
• No men in suits please. I don't want this to have a 1980s corporate look.

```html
<!DOCTYPE html>
<html lang="en">
<head>
<meta charset="utf-8">
<title>Climb and Glow – Book Cover Wrap</title>
<link rel="stylesheet" href="https://fonts.googleapis.com/css2?family=Bebas+Neue&family=Roboto+Condensed:wght@400&display=swap">
<style>
  :root {
    --ink: #000000;
    --paper: #ffffff;
    --brand-orange: #f78f20;
    --megaphone-grey: #5a5d66;
    --megaphone-light: #e9eaee;
  }
  html, body {
    margin: 0;
    padding: 0;
    width: 1200px;
    height: 900px;
    overflow: hidden;
    background: var(--ink);
  }
  .cover-wrap {
    position: relative;
    width: 1200px;
    height: 900px;
    background: var(--ink);
    overflow: hidden;
    font-family: "Bebas Neue", "Oswald", sans-serif;
  }
  .bubble-shapes {
    position: absolute;
    inset: 0;
  }

  /* Back cover */
  .back-title {
    position: absolute;
    left: 37px;
    top: 30px;
    margin: 0;
    font-size: 62px;
    line-height: 1;
    font-weight: 400;
    color: var(--brand-orange);
    letter-spacing: 0.5px;
  }
  .back-subtitle {
    position: absolute;
    left: 37px;
    top: 93px;
    width: 530px;
    margin: 0;
    font-size: 29px;
    line-height: 1;
    font-weight: 400;
    color: var(--ink);
    white-space: nowrap;
  }
  .back-blurb {
    position: absolute;
    left: 40px;
    top: 366px;
    width: 522px;
    margin: 0;
    font-family: "Roboto Condensed", "Arial Narrow", sans-serif;
    font-size: 15px;
    line-height: 20px;
    color: var(--paper);
    text-align: center;
  }
  .back-blurb p {
    margin: 0 0 20px;
  }
  .publisher-mark {
    position: absolute;
    left: 45px;
    top: 758px;
    width: 99px;
    height: 70px;
    background: var(--paper);
    display: flex;
    flex-direction: column;
    align-items: center;
    justify-content: center;
    font-size: 24px;
    line-height: 0.95;
    color: var(--brand-orange);
  }
  .barcode-area {
    position: absolute;
    left: 357px;
    top: 732px;
    width: 200px;
    height: 120px;
    background: var(--paper);
  }

  /* Spine */
  .spine-text {
    position: absolute;
    left: 575px;
    writing-mode: vertical-rl;
    margin: 0;
    font-weight: 400;
    color: var(--brand-orange);
    line-height: 46px;
    width: 46px;
    font-size: 45px;
  }
  .spine-title {
    top: 60px;
  }
  .spine-author {
    top: 580px;
  }

  /* Front cover */
  .front-title {
    position: absolute;
    left: 758px;
    top: 60px;
    margin: 0;
    font-weight: 400;
    color: var(--brand-orange);
    line-height: 0.86;
  }
  .front-title .word-main {
    display: block;
    font-size: 150px;
  }
  .front-title .word-and {
    position: absolute;
    left: 284px;
    top: 12px;
    writing-mode: vertical-rl;
    transform: rotate(180deg);
    font-size: 84px;
    line-height: 0.82;
  }
  .megaphone-art {
    position: absolute;
    left: 640px;
    top: 390px;
    width: 270px;
    height: 280px;
    border-radius: 16px;
    background: linear-gradient(135deg, var(--megaphone-light) 0%, var(--megaphone-grey) 100%);
  }
  .front-subtitle {
    position: absolute;
    left: 955px;
    top: 396px;
    width: 215px;
    margin: 0;
    font-size: 44px;
    line-height: 46px;
    font-weight: 400;
    color: var(--ink);
    text-align: center;
  }
  .front-subtitle span {
    display: block;
  }
  .front-author {
    position: absolute;
    left: 700px;
    top: 786px;
    width: 440px;
    margin: 0;
    font-size: 76px;
    line-height: 1;
    font-weight: 400;
    color: var(--brand-orange);
    text-align: center;
  }
</style>
</head>
<body>
<main class="cover-wrap">
  <svg class="bubble-shapes" width="1200" height="900" viewBox="0 0 1200 900" aria-hidden="true">
    <path class="back-bubble" fill="#ffffff"
      d="M0 0 H576 V196 Q560 226 530 252 L220 232 L198 343 L50 200 L0 192 Z"/>
    <path class="front-bubble" fill="#ffffff"
      d="M992 340 H1190 V727 H990 Q950 712 938 692 L955 583 L846 474 L982 378 Z"/>
  </svg>

  <!-- Back cover -->
  <h2 class="back-title">Climb and Glow</h2>
  <p class="back-subtitle">Find Your Voice. Tell Your Story. Share Your Message.</p>
  <div class="back-blurb">
    <p>Lorem ipsum dolor sit amet, consectetur adipisicing elit, sed do eiusmod tempor incididunt ut labore et dolore magna aliqua. Ut enim ad minim veniam, quis nostrud exercitation ullamco laboris nisi ut aliquip ex ea commodo consequat.</p>
    <p>Duis aute irure dolor in reprehenderit in voluptate velit esse cillum dolore eu fugiat nulla pariatur. Excepteur sint occæcat cupidatat non proident, sunt in culpa qui officia deserunt mollit anim id est laborum. Sed ut perspiciatis unde omnis iste natus error sit voluptatem accusantium doloremque laudantium, totam rem aperiam, eaque ipsa quæ ab illo inventore veritatis et quasi architecto beatæ vitæ dicta sunt explicabo.</p>
    <p>Nemo enim ipsam voluptatem quia voluptas sit aspernatur aut odit aut fugit, sed quia consequuntur magni dolores eos qui ratione voluptatem sequi nesciunt. Neque porro quisquam est, qui dolorem ipsum quia dolor sit amet, consectetur, adipisci velit, sed quia non numquam eius modi tempora incidunt ut labore et dolore magnam aliquam quærat voluptatem.</p>
  </div>
  <div class="publisher-mark"><span>Parcelo</span><span>Leafbook</span></div>
  <div class="barcode-area"></div>

  <!-- Spine -->
  <p class="spine-text spine-title">CLIMB AND GLOW</p>
  <p class="spine-text spine-author">LIONEL BARSTOW</p>

  <!-- Front cover -->
  <h1 class="front-title">
    <span class="word-main">CLIMB</span>
    <span class="word-and">AND</span>
    <span class="word-main">GLOW</span>
  </h1>
  <div class="megaphone-art" role="img" aria-label="Illustration of a hand holding a megaphone with sound lines"></div>
  <p class="front-subtitle">
    <span>FIND YOUR</span><span>VOICE.</span>
    <span>TELL YOUR</span><span>STORY.</span>
    <span>SHARE YOUR</span><span>MESSAGE.</span>
  </p>
  <p class="front-author">LIONEL BARSTOW</p>
</main>
</body>
</html>
```